Business card, postcard, pocket folder

We are a real estate team and have had a new logo designed. From this, we need the following deliverables:- Business Cards (double-sided)- Just Listed / Just Sold Postcards (double-sided)- Pocket Folder. See logo attached.More work possible for the winning designer.
There are 5 members of the team, so head shots should be easily changed and possible for a group photo might be a good idea for the pocket folder but not 100% neccessary.
Target Market(s)
Real estate
Industry/Entity Type
Real Estate
Font styles to use
Serif
Sans Serif
Requirements
Must have
- Business cards and postcards must have a head shot on them.

```html
<!DOCTYPE html>
<html lang="en">
<head>
<meta charset="utf-8">
<title>Hartwell Group – Business Card</title>
<link rel="stylesheet" href="https://fonts.googleapis.com/css2?family=Montserrat:ital,wght@0,400;0,500;0,700;1,400&display=swap">
<style>
  :root {
    --red: #c30007;
    --blue: #1f2f9a;
    --black: #1b1b1b;
    --white: #ffffff;
    --paper: #f1f1f1;
    --ink: #222222;
    --bg: #e9e6e1;
  }
  * { box-sizing: border-box; margin: 0; padding: 0; }
  html, body { width: 1200px; height: 858px; overflow: hidden; }
  body {
    background: var(--bg);
    font-family: "Montserrat", Arial, sans-serif;
    position: relative;
  }
  .card {
    position: absolute;
    width: 540px;
    height: 310px;
    overflow: hidden;
    box-shadow: 0 6px 18px rgba(0,0,0,.18);
  }
  .card svg.card-art { position: absolute; inset: 0; }
  .card-front { left: 50px; top: 150px; background: var(--red); }
  .card-back { left: 610px; top: 398px; background: var(--paper); }

  .brand-name {
    position: absolute;
    text-align: center;
    font-weight: 700;
    letter-spacing: .5px;
    white-space: nowrap;
  }
  .card-front .brand-name { left: 0; right: 0; top: 128px; font-size: 40px; color: var(--blue); }
  .card-back .brand-name { left: 10px; width: 270px; top: 136px; font-size: 28px; color: var(--white); }

  .front-web {
    position: absolute;
    left: 0; right: 0; top: 262px;
    display: flex; justify-content: center; align-items: center; gap: 8px;
    color: var(--white);
    font-size: 13px;
    letter-spacing: 1px;
  }

  .contact {
    position: absolute;
    left: 372px; top: 38px;
    width: 160px;
    color: var(--ink);
  }
  .headshot {
    width: 72px; height: 72px;
    background: linear-gradient(180deg, #dedede, #c4c4c4);
    border-radius: 3px;
    margin-left: 14px;
  }
  .person-name { margin-top: 14px; color: var(--red); font-weight: 700; font-size: 15px; white-space: nowrap; }
  .person-title { font-style: italic; font-size: 12px; margin-bottom: 14px; }
  .contact-line {
    display: grid;
    grid-template-columns: 10px auto;
    column-gap: 6px;
    align-items: center;
    font-size: 10px;
    line-height: 12px;
    margin-bottom: 8px;
    white-space: nowrap;
  }
  .dot { width: 10px; height: 10px; border-radius: 50%; background: var(--blue); }
  .socials { display: flex; align-items: center; gap: 7px; font-size: 10.5px; margin-top: 4px; white-space: nowrap; }
  .socials-label { margin-right: 2px; }
  .social { width: 14px; height: 14px; border-radius: 50%; flex: none; }
  .social-blue { background: var(--blue); }
  .social-red { background: var(--red); }
</style>
</head>
<body>

<section class="card card-front">
  <svg class="card-art" width="540" height="310" viewBox="0 0 540 310" aria-hidden="true">
    <defs>
      <linearGradient id="band" x1="0" x2="1" y1="0" y2="0">
        <stop offset="0" stop-color="#dcdcdc"/>
        <stop offset=".5" stop-color="#ffffff"/>
        <stop offset="1" stop-color="#dcdcdc"/>
      </linearGradient>
    </defs>
    <path d="M0,110 L160,110 C200,110 215,62 270,60 C325,62 340,110 380,110 L540,110 L540,200 L380,200 C340,200 325,250 270,252 C215,250 200,200 160,200 L0,200 Z"
          fill="url(#band)"/>
    <path d="M0,100 L155,100 C195,100 212,50 270,48 C328,50 345,100 385,100 L540,100" fill="none" stroke="#fff" stroke-width="2"/>
    <path d="M0,210 L155,210 C195,210 212,262 270,264 C328,262 345,210 385,210 L540,210" fill="none" stroke="#fff" stroke-width="2"/>
  </svg>
  <div class="brand-name">Hartwell Group</div>
  <div class="front-web">
    <svg width="14" height="14" viewBox="0 0 14 14" aria-hidden="true">
      <circle cx="7" cy="7" r="6" fill="none" stroke="#fff" stroke-width="1.2"/>
      <ellipse cx="7" cy="7" rx="2.6" ry="6" fill="none" stroke="#fff" stroke-width="1"/>
      <line x1="1" y1="7" x2="13" y2="7" stroke="#fff" stroke-width="1"/>
    </svg>
    <span>WEB ADDRESS GOES HERE</span>
  </div>
</section>

<section class="card card-back">
  <svg class="card-art" width="540" height="310" viewBox="0 0 540 310" aria-hidden="true">
    <defs>
      <linearGradient id="paper" x1="0" x2="1">
        <stop offset="0" stop-color="#ffffff"/>
        <stop offset="1" stop-color="#e4e4e4"/>
      </linearGradient>
    </defs>
    <rect width="540" height="310" fill="url(#paper)"/>
    <polygon points="0,0 272,0 346,190 236,310 0,310" fill="var(--red)"/>
    <polygon points="0,0 256,0 330,190 220,310 0,310" fill="#fff"/>
    <polygon points="0,0 248,0 320,190 210,310 0,310" fill="var(--black)"/>
  </svg>
  <div class="brand-name">Hartwell Group</div>

  <div class="contact">
    <div class="headshot" role="img" aria-label="Team member head shot"></div>
    <div class="person-name">Name Goes Here</div>
    <div class="person-title">Designation</div>
    <div class="contact-line"><span class="dot"></span><span>123 456 789</span></div>
    <div class="contact-line"><span class="dot"></span><span>Email Address Goes Here</span></div>
    <div class="contact-line"><span class="dot"></span><span>Web Address Goes Here</span></div>
    <div class="socials">
      <span class="socials-label">Visit us on :</span>
      <span class="social social-blue"></span>
      <span class="social social-red"></span>
      <span class="social social-blue"></span>
      <span class="social social-red"></span>
    </div>
  </div>
</section>

</body>
</html>
```